KVT Wellness Co Business Card for food and Beverage Falcons & Lanterns

One main business card design for a wellness enterprise which represents two brands. We need one primary card design, for two different employees. The only difference between the cards will be the name, title and phone number for each employee, all other design elements will be same.
I've uploaded the logos for each brand. I have also uploaded a mockup which I made using Google's drawing tool. I can provide example images of business cards we find attractive if you would like some help picturing what we like.
I'm picturing the color splash on the back of the card below the two logos to be a dark burgundy or blue. This may sound a bit silly but the feel of the card and color should look almost like wizard dress robes. Dark emerald green, dark blue and dark burgundy with black undertones and gold lace.
Updates

Reason: Thank you all for the submissions. I will need some extra time to give you feedback. Cheers

Target Market(s)

Healthy food and beverage industry

Industry/Entity Type

Health And Wellness

Contact Information for Business Card

On one side we would like the business name, location, title of employee, employee name and contact details. On the flip side we would like our two brand logos and a splash of color. We would like the card to have a black font with some gold accents if possible. We would also like the trim of the business card or a middle ply within the card stock to have a color other than white.

Font styles to use
Serif

Colors
ec1f27
0255a3
00a990

Requirements
Must have
• Bold dark colors, happy to provide sample photos of business cards I like from clipnook. Must have a version for two different employees. Must be sharp, modern and chic.
Nice to have
• Thick card stock layer in between the front and back of card that is either black or gold lace or something to make it feel, well let's say to make it feel expensive.
Should not have
• Should not have any cartoon-ey elements. All business.

```html
<!DOCTYPE html>
<html lang="en">
<head>
<meta charset="utf-8">
<title>KVT Wellness Co – Business Card</title>
<link rel="stylesheet" href="https://fonts.googleapis.com/css2?family=Source+Sans+3:wght@400;600&display=swap">
<style>
  :root {
    --stage: #666666;
    --card: #000000;
    --ink-light: #dcdcdc;
    --ink-white: #ffffff;
    --gold: #e0a100;
    --burgundy: #5e0a1f;
    --ochre: #c49a12;
  }
  html, body {
    margin: 0;
    width: 1200px;
    height: 900px;
    overflow: hidden;
    background: var(--stage);
    font-family: "Source Sans 3", sans-serif;
  }
  .stage { position: relative; width: 1200px; height: 900px; }
  .card {
    position: absolute;
    top: 170px;
    width: 347px;
    height: 561px;
    background: var(--card);
    overflow: hidden;
    text-align: center;
  }
  .card-front { left: 259px; }
  .card-back { left: 649px; }

  .company-name {
    position: absolute; top: 57px; left: 0; right: 0;
    margin: 0; font-size: 24px; line-height: 30px; font-weight: 600; color: var(--ink-light);
  }
  .company-location {
    position: absolute; top: 87px; left: 0; right: 0;
    margin: 0; font-size: 17px; line-height: 22px; color: var(--ink-light);
  }
  .employee-name {
    position: absolute; top: 350px; left: 0; right: 0;
    margin: 0; font-size: 24px; line-height: 30px; font-weight: 600; color: var(--gold);
  }
  .employee-title {
    position: absolute; top: 378px; left: 0; right: 0;
    margin: 0; font-size: 16px; line-height: 22px; color: var(--ink-light);
  }
  .contact-icons {
    position: absolute; top: 429px; left: 0; right: 0;
    display: flex; justify-content: center; gap: 5px;
  }
  .contact-icons svg { width: 21px; height: 21px; }
  .contact-line {
    position: absolute; left: 0; right: 0; margin: 0;
    font-size: 18px; line-height: 23px; color: var(--ink-white);
  }
  .contact-phone { top: 455px; }
  .contact-email { top: 478px; }

  .brand-name {
    position: absolute; left: 0; right: 0; margin: 0;
    font-size: 22px; font-weight: 600; color: var(--ink-white);
  }
  .brand-primary { top: 96px; }
  .brand-secondary { top: 276px; }
  .color-splash {
    position: absolute; left: 0; bottom: 0; width: 347px; height: 240px;
  }
</style>
</head>
<body>
<main class="stage">
  <section class="card card-front" aria-label="Card front">
    <h1 class="company-name">KVT Wellness Co</h1>
    <p class="company-location">Larkmoor,CA</p>
    <h2 class="employee-name">Marcus Ellery</h2>
    <p class="employee-title">Beverage Alchemist</p>
    <div class="contact-icons">
      <svg viewBox="0 0 20 20" aria-label="Phone">
        <circle cx="10" cy="10" r="10" fill="var(--gold)"/>
        <path d="M7 5.5l1.6 2.2-1 1.2a7 7 0 0 0 3.5 3.5l1.2-1 2.2 1.6-.8 1.6c-3.8.2-8-4-7.8-7.8z" fill="#000"/>
      </svg>
      <svg viewBox="0 0 20 20" aria-label="Email">
        <circle cx="10" cy="10" r="10" fill="var(--gold)"/>
        <rect x="5" y="6.5" width="10" height="7" fill="#000"/>
        <path d="M5 6.5l5 4 5-4" fill="none" stroke="var(--gold)" stroke-width="1"/>
      </svg>
    </div>
    <p class="contact-line contact-phone">415.555.0182</p>
    <p class="contact-line contact-email">kvtwellnessco@postwell.com</p>
  </section>

  <section class="card card-back" aria-label="Card back">
    <p class="brand-name brand-primary">KVT Wellness Co</p>
    <p class="brand-name brand-secondary">Falcons &amp; Lanterns</p>
    <svg class="color-splash" viewBox="0 0 347 240" role="img" aria-label="Textured burgundy and gold paint splash">
      <defs>
        <linearGradient id="splash-tone" x1="0" y1="0" x2="1" y2="1">
          <stop offset="0" stop-color="var(--ochre)"/>
          <stop offset="0.3" stop-color="var(--burgundy)"/>
          <stop offset="0.75" stop-color="var(--burgundy)"/>
          <stop offset="1" stop-color="var(--ochre)"/>
        </linearGradient>
      </defs>
      <path d="M0 88 L40 92 L90 98 L130 100 L175 88 L215 70 L260 52 L300 34 L347 4 L347 240 L0 240 Z" fill="url(#splash-tone)"/>
    </svg>
  </section>
</main>
</body>
</html>
```